Need posters that inspire entrepreneurs

I want to create beautiful, inspiring wall art. I'm looking for a designer to create an awesome sample (note this sample is not for real use). The winning design will form the foundation of our art "style" so there will be LOTS of ongoing work for the winning designer.

It's your challenge to create a style that is clean, inspiring and timeless, and possibly can be adapted to different colour palettes.

Looking for a perfect execution of words, image and design.

The attached example shows one idea. It should serve as an idea only.

Format of the images should be either rectangular or square. Exact size is preferably UK A4 (US letter) or max A3. Assume that a display would consist of a 4 x 4 image grid so size needs to allow for that in a small to medium size office.

The quotes I want in the 3 samples (each in an individual poster - not combined in 1 poster). Each quote should have it's own, the reason for three is to prove the design work on more than one quote. The quotes are:

1) Failure is the condiment that gives success its flavor.
– Dorian Welsby

2) Whether you think you can or think you can’t, you’re right.
– Oswald Pike

3) Ever tried. Ever failed. No matter. Try Again. Fail again. Fail better.
– Lionel Marwick

Each design should include the image of the person and the quote + any design elements you consider relevant. You should find relevant images of the individuals being quoted. The final images will not be published or used commercially in any way.

Font styles to use
Serif
Sans Serif

Colors

Designer to choose colors to be used in the design.

Requirements
Must have
• Words and headshot image - 1 per poster design.
• Please consider in the design that there will not always be photographs of the person quoted and as such the design will need to hold, whether the source is a photo, sketch or something else.
Nice to have
• None, but note that the final image will be printed on a wall mounted board, printed to the edge but not on the edge. The board will have black or white edges so consider in the design.
Should not have
• None

```html
<!DOCTYPE html>
<html lang="en">
<head>
<meta charset="utf-8">
<title>Entrepreneur Quote Posters</title>
<link rel="stylesheet" href="https://fonts.googleapis.com/css2?family=Roboto+Slab:wght@800;900&family=Roboto+Condensed:wght@700&family=Cinzel:wght@700&display=swap">
<style>
  :root {
    --band: #161616;
    --wall: #3a3a3a;
    --poster-edge: #f4f4f4;
    --photo-light: #e9e9e9;
    --photo-mid: #bdbdbd;
    --photo-dark: #8c8c8c;
    --ink: #141414;
    --accent-red: #c8102e;
  }
  * { box-sizing: border-box; margin: 0; padding: 0; }
  html, body {
    width: 1200px;
    height: 599px;
    overflow: hidden;
    background: var(--band);
  }
  .presentation {
    position: relative;
    width: 1200px;
    height: 599px;
    background: var(--band);
  }
  .presentation-wall {
    position: absolute;
    left: 0;
    top: 58px;
    width: 1200px;
    height: 482px;
    background: var(--wall);
  }
  .presentation-label {
    position: absolute;
    right: 15px;
    bottom: 18px;
    font-family: "Cinzel", "Times New Roman", serif;
    font-weight: 700;
    font-size: 23px;
    line-height: 1;
    letter-spacing: 0.5px;
    color: var(--accent-red);
  }
  .poster {
    position: absolute;
    top: 130px;
    width: 258px;
    height: 362px;
    background: var(--poster-edge);
    box-shadow: 0 2px 8px rgba(0,0,0,0.5);
  }
  .poster--marwick { left: 87px; }
  .poster--pike { left: 471px; }
  .poster--welsby { left: 853px; }
  .poster-photo {
    position: absolute;
    inset: 6px;
    background:
      radial-gradient(ellipse 38% 55% at 62% 62%, var(--photo-dark) 0%, rgba(140,140,140,0) 100%),
      linear-gradient(180deg, var(--photo-mid) 0%, var(--photo-light) 55%, var(--photo-mid) 100%);
  }
  .poster-credit {
    position: absolute;
    left: 19px;
    bottom: 20px;
    width: 12px;
    font-family: "Roboto Condensed", "Arial Narrow", Arial, sans-serif;
    font-weight: 700;
    font-size: 11px;
    letter-spacing: 0.3px;
    color: var(--accent-red);
    text-transform: uppercase;
    white-space: nowrap;
    writing-mode: vertical-rl;
    transform: rotate(180deg);
  }
  .poster-quote {
    position: absolute;
    left: 37px;
    bottom: 16px;
    font-family: "Roboto Slab", "Rockwell Extra Bold", Rockwell, "Arvo", serif;
    font-weight: 900;
    font-size: 21px;
    line-height: 24.5px;
    letter-spacing: -0.2px;
    color: var(--ink);
    white-space: nowrap;
  }
  .poster--welsby .poster-quote { left: 40px; bottom: 14px; }
  .poster--welsby .poster-credit { left: 20px; bottom: 16px; }
</style>
</head>
<body>
  <main class="presentation">
    <div class="presentation-wall"></div>

    <article class="poster poster--marwick">
      <div class="poster-photo" role="img" aria-label="Black and white portrait of Lionel Marwick in a jacket and turtleneck over a faded photo collage"></div>
      <p class="poster-credit">Lionel Marwick</p>
      <p class="poster-quote">Ever tried,<br>Ever failed,<br>No matter,<br>Try Again,<br>Fail again,<br>Fail better</p>
    </article>

    <article class="poster poster--pike">
      <div class="poster-photo" role="img" aria-label="Black and white portrait of Oswald Pike in a bowler hat and overcoat over a faded photo collage"></div>
      <p class="poster-credit">Oswald Pike</p>
      <p class="poster-quote">Whether<br>you think<br>you can<br>or think<br>you can’t,<br>you’re right</p>
    </article>

    <article class="poster poster--welsby">
      <div class="poster-photo" role="img" aria-label="Black and white portrait of Dorian Welsby in glasses and a dark suit over a faded photo collage"></div>
      <p class="poster-credit">Dorian Welsby</p>
      <p class="poster-quote">Failure<br>is the<br>condiment<br>that gives<br>success<br>its flavor.</p>
    </article>

    <p class="presentation-label">POSTER DESIGNS</p>
  </main>
</body>
</html>
```